Torvane Aviation Limited

Started a consulting business 12 months ago and have since moved location and have grown and seek to identify my self to the industry.
Specializing in quality solutions, business documentation and maintenance solution's

Industry/Entity Type

Business

```html
<!DOCTYPE html>
<html lang="en">
<head>
<meta charset="utf-8">
<title>Torvane Aviation Limited – Business Card</title>
<link rel="stylesheet" href="https://fonts.googleapis.com/css2?family=Comfortaa:wght@700&family=Exo+2:wght@400;500&display=swap">
<style>
  :root {
    --page-bg: #e8e6e3;
    --card-light: #ffffff;
    --card-shade: #e4e4e4;
    --ink: #1e1e1e;
    --ink-soft: #3a3a3a;
    --band-dark: #1f1f1f;
    --band-green: #9ccd2c;
    --on-dark: #ffffff;
  }
  * { margin: 0; padding: 0; box-sizing: border-box; }
  html, body {
    width: 1200px; height: 899px; overflow: hidden;
    background: var(--page-bg);
  }
  .stage { position: relative; width: 1200px; height: 899px; }
  .card {
    position: absolute; left: 290px; width: 620px; height: 354px;
    background: radial-gradient(ellipse at 45% 40%, var(--card-light) 0%, var(--card-light) 35%, var(--card-shade) 100%);
    box-shadow: 0 6px 18px rgba(0,0,0,0.22);
    overflow: hidden;
  }
  .card-front { top: 70px; }
  .card-back { top: 475px; }
  .brand-name {
    font-family: "Comfortaa", sans-serif; font-weight: 700;
    color: var(--ink); white-space: nowrap; letter-spacing: -0.5px;
  }
  .card-front .brand-name {
    position: absolute; left: 0; right: 0; top: 152px;
    text-align: center; font-size: 38px;
  }
  .card-back .brand-name {
    position: absolute; left: 42px; top: 176px; font-size: 30px;
  }
  .wave { position: absolute; left: 0; top: 0; width: 620px; height: 354px; }
  .contact {
    position: absolute; left: 398px; top: 38px;
    font-family: "Exo 2", sans-serif; font-size: 12px; color: var(--ink-soft);
  }
  .contact-address { line-height: 15px; margin-bottom: 18px; letter-spacing: 0.3px; }
  .contact-list { list-style: none; }
  .contact-list li { display: flex; align-items: center; height: 18px; }
  .contact-list svg { width: 11px; height: 11px; margin-right: 8px; fill: var(--ink-soft); }
  .person {
    position: absolute; left: 372px; top: 262px;
    font-family: "Exo 2", sans-serif; color: var(--on-dark);
  }
  .person-name { font-size: 19px; font-weight: 500; letter-spacing: 1.5px; }
  .person-role { font-size: 15px; margin-left: 30px; letter-spacing: 0.4px; }
</style>
</head>
<body>
<main class="stage">
  <section class="card card-front" aria-label="Card front">
    <p class="brand-name">Torvane Aviation Limited</p>
  </section>

  <section class="card card-back" aria-label="Card back">
    <svg class="wave" viewBox="0 0 620 354" aria-hidden="true">
      <path d="M0,312 C160,312 262,294 342,246 C422,198 520,176 620,172 L620,354 L0,354Z" fill="var(--band-green)"/>
      <path d="M0,338 C160,336 272,318 352,268 C432,220 530,198 620,194 L620,354 L0,354Z" fill="var(--band-dark)" stroke="#ffffff" stroke-width="4"/>
    </svg>

    <p class="brand-name">Torvane Aviation Limited</p>

    <div class="contact">
      <p class="contact-address">Unit 4, Hangar Row<br>Westfield Airpark</p>
      <ul class="contact-list">
        <li><svg viewBox="0 0 12 12"><path d="M2.5 0.5l2 2.4-1.2 1.4c.7 1.6 2 2.9 3.6 3.6l1.4-1.2 2.4 2-1.3 2.3C4.6 10.5 1.5 7.4 0.5 2.1z"/></svg>020 481 7356</li>
        <li><svg viewBox="0 0 12 12"><path d="M3 0h6v12H3z M4 1.5v8h4v-8z"/></svg>020 481 7357</li>
        <li><svg viewBox="0 0 12 12"><path d="M3 0h5v3H3z M1 4h10v7H1z M3 6v1h6V6z"/></svg>020 481 7358</li>
        <li><svg viewBox="0 0 12 12"><path d="M0 2h12v8H0z M0.8 2.6L6 6.6l5.2-4z" fill-rule="evenodd"/></svg>info@torvaneaviation.com</li>
        <li><svg viewBox="0 0 12 12"><path d="M6 0a6 6 0 1 0 0 12A6 6 0 0 0 6 0zm0 1.2c.9 1 1.5 2.7 1.6 4.2H4.4C4.5 3.9 5.1 2.2 6 1.2zM1.3 5.4h2c.1-1.5.5-2.9 1.1-3.9a4.8 4.8 0 0 0-3.1 3.9zm0 1.2a4.8 4.8 0 0 0 3.1 3.9c-.6-1-1-2.4-1.1-3.9zm3.1 0h3.2c-.1 1.5-.7 3.2-1.6 4.2-.9-1-1.5-2.7-1.6-4.2zm4.3 0c-.1 1.5-.5 2.9-1.1 3.9a4.8 4.8 0 0 0 3.1-3.9zm2-1.2a4.8 4.8 0 0 0-3.1-3.9c.6 1 1 2.4 1.1 3.9z"/></svg>www.torvaneaviation.com</li>
      </ul>
    </div>

    <div class="person">
      <p class="person-name">MARCUS HELLER</p>
      <p class="person-role">Managing Director</p>
    </div>
  </section>
</main>
</body>
</html>
```